K9 Orbit needs a business card designed

We need a business card designed for K9 Orbit, an expansion of K9 Systems Pty Ltd (www.k9systems.com.au)

We provide high quality professional services for the Australian space industry. Our clients include the Southern Launch Bureau and companies working in the space industry. We identify people with space related skills both locally and internationally who are then contracted by clients to create products and support space launch activities.

Colours to be used:
- Navy blue #000080
- Rocket metallic #8A7F8D
- Platinum #E5E4E2
- Black #000000
- White #FFFFFF

*Front of the card*
I have attached our K9 Orbit logo, which needs to be the main item on the card. The 'Space' text should be placed to the right of the 'K9' part rather than below, similar to the attached K9 Systems card, which this card should match.

If subtext is included, however, it should read ‘Labour Hire • Consultancy • Project Delivery’ rather than the ‘Design • Build • Test • Maintain’ of the K9 Systems card.

A black background (rather than blue background in the K9 Systems card) might be good, with a white pattern as in the K9 Systems card. If colour is used, the logo should be in its standard colours (as provided for the K9 Orbit logo).

*Back of the card*
Include a smaller K9 Orbit logo on the back.

We need the following details for K9 Orbit personnel (as a template for entry):
- Name
- Company Position
- Mobile Number
- Email
- Office Address
- Include the K9 Orbit website: www.k9orbit.com.au

Overall, we'd like to see a design that communicates the adventure of space, professional integrity, and customer service. We look forward to seeing what you can come up with.

Target Market(s)

We provide high quality professional services for the Australian space industry. Our clients include the Southern Launch Bureau and companies working in the space industry.

Contact Information for Business Card

- Name
- Company Position
- Mobile Number
- Email
- Office Address

Requirements
Must have
• See project description.

```html
<!DOCTYPE html>
<html lang="en">
<head>
<meta charset="utf-8">
<title>K9 Orbit – Business Card</title>
<link href="https://fonts.googleapis.com/css2?family=Quicksand:wght@400;500;600&family=Roboto:wght@400;500&family=Roboto+Condensed:wght@700&display=swap" rel="stylesheet">
<style>
  :root {
    --stage: #d1d2d4;
    --navy: #27296f;
    --rocket: #8a7f8d;
    --black: #000000;
    --charcoal: #2f2c30;
    --white: #ffffff;
  }
  * { margin: 0; padding: 0; box-sizing: border-box; }
  html, body { width: 962px; height: 1200px; overflow: hidden; }
  body { background: var(--stage); position: relative; }

  .card {
    position: absolute;
    left: 117px;
    width: 730px;
    height: 438px;
    overflow: hidden;
  }
  .card-front { top: 149px; background: var(--black); }
  .card-back { top: 613px; background: var(--white); }

  .front-backdrop {
    position: absolute;
    inset: 0;
    background:
      radial-gradient(ellipse 55% 45% at 88% 8%, rgba(39, 41, 111, 0.9) 0%, rgba(39, 41, 111, 0) 100%),
      radial-gradient(ellipse 60% 40% at 18% 100%, rgba(138, 127, 141, 0.75) 0%, rgba(138, 127, 141, 0) 100%),
      radial-gradient(ellipse 60% 90% at 52% 35%, var(--charcoal) 0%, #141214 55%, var(--black) 100%);
  }
  .back-accent {
    position: absolute;
    top: 0; right: 0;
    width: 300px; height: 100%;
    background:
      radial-gradient(ellipse 70% 60% at 100% 25%, rgba(39, 41, 111, 0.85) 0%, rgba(39, 41, 111, 0) 100%),
      radial-gradient(ellipse 60% 55% at 100% 90%, rgba(138, 127, 141, 0.75) 0%, rgba(138, 127, 141, 0) 100%);
  }

  .front-wordmark {
    position: absolute;
    left: 0; right: 0;
    top: 145px;
    text-align: center;
    font-family: "Quicksand", sans-serif;
    font-weight: 600;
    font-size: 62px;
    letter-spacing: 14px;
    color: var(--white);
    line-height: 1;
  }
  .front-tagline {
    position: absolute;
    left: 0; right: 0;
    top: 248px;
    text-align: center;
    font-family: "Quicksand", sans-serif;
    font-weight: 400;
    font-size: 21px;
    line-height: 26px;
    letter-spacing: 0.3px;
    color: var(--white);
  }

  .back-wordmark {
    position: absolute;
    left: 30px;
    width: 270px;
    top: 192px;
    text-align: center;
    font-family: "Quicksand", sans-serif;
    font-weight: 600;
    font-size: 48px;
    letter-spacing: 4px;
    color: var(--navy);
    line-height: 1;
  }
  .divider {
    position: absolute;
    left: 314px; top: 138px;
    width: 3px; height: 186px;
    background: var(--navy);
  }
  .divider::before {
    content: "";
    position: absolute;
    left: -7px; top: 86px;
    border-top: 7px solid transparent;
    border-bottom: 7px solid transparent;
    border-right: 7px solid var(--navy);
  }

  .details { position: absolute; left: 350px; top: 0; font-family: "Roboto", sans-serif; color: var(--navy); }
  .details > * { position: absolute; left: 0; white-space: nowrap; line-height: 1; }
  .person-name { top: 79px; font-family: "Roboto Condensed", sans-serif; font-weight: 700; font-size: 34px; color: var(--rocket); }
  .person-position { top: 116px; font-size: 22px; }
  .address-label { top: 167px; font-family: "Roboto Condensed", sans-serif; font-weight: 700; font-size: 27px; color: var(--rocket); }
  .address-line { font-size: 21px; }
  .address-line.one { top: 199px; }
  .address-line.two { top: 225px; }
  .contact { display: flex; align-items: center; gap: 8px; font-size: 21px; }
  .contact svg { width: 22px; height: 20px; flex: none; }
  .contact.phone { top: 286px; }
  .contact.email { top: 312px; }
  .contact.web { top: 338px; }
</style>
</head>
<body>

<section class="card card-front">
  <div class="front-backdrop" role="img" aria-label="Navy and mauve orbital swoosh pattern on a dark background"></div>
  <div class="front-wordmark">K9 ORBIT</div>
  <p class="front-tagline">Labour Hire • Consultancy • Project Delivery’ rather than<br>the ‘Design • Build • Test • Maintain’<br>of the K9 Systems card.</p>
</section>

<section class="card card-back">
  <div class="back-accent" role="img" aria-label="Navy and mauve orbital swoosh with small stars"></div>

  <div class="back-wordmark">K9 Orbit</div>
  <div class="divider"></div>

  <div class="details">
    <div class="person-name">Name</div>
    <div class="person-position">Company Position</div>
    <div class="address-label">Office Address</div>
    <div class="address-line one">xxxxxxxxxxx</div>
    <div class="address-line two">xxxxxxxxxxxxxxxxxxxxxx</div>
    <div class="contact phone">
      <svg viewBox="0 0 22 20" aria-hidden="true"><rect x="6" y="2" width="9" height="16" rx="1.5" transform="rotate(35 11 10)" fill="none" stroke="var(--rocket)" stroke-width="1.6"/></svg>
      <span>: xxxxxxxxxxxxxxx</span>
    </div>
    <div class="contact email">
      <svg viewBox="0 0 22 20" aria-hidden="true"><path d="M2,9 L12,3 L20,9 L12,17 Z" fill="var(--rocket)"/><path d="M2,9 L12,11 L20,9" fill="none" stroke="var(--white)" stroke-width="1.2"/></svg>
      <span>: xxxxxxxxxxxxxxxxxxxxxxx</span>
    </div>
    <div class="contact web">
      <svg viewBox="0 0 22 20" aria-hidden="true"><g fill="none" stroke="var(--rocket)" stroke-width="1.3"><circle cx="11" cy="10" r="8"/><ellipse cx="11" cy="10" rx="3.5" ry="8"/><path d="M3,10 H19 M4.5,6 H17.5 M4.5,14 H17.5"/></g></svg>
      <span>: www.k9orbit.com.au</span>
    </div>
  </div>
</section>

</body>
</html>
```